Flooring & Interior Design showroom

Just bought this business- Kestrel Lane Flooring & Interiors. Love our logo (we are on Kestrel Lane )and colors
Forest green, gold and black
Love that the back lists everything we do. We no longer have plenotilex but need to add in LVP/ SPC and need to take out vantor shadehub logo at the bottom and use the quib logo instead (maybe? open to suggestions)

Not in love with our cards- I want a higher end look
I hate the gradient poop color we have now.
Would love if they were all black - maybe or ??
or had a foil or embossing?

```html
<!DOCTYPE html>
<html lang="en">
<head>
<meta charset="utf-8">
<title>Kestrel Lane Flooring &amp; Interiors — Business Cards</title>
<link rel="stylesheet" href="https://fonts.googleapis.com/css2?family=Cormorant+Garamond:ital,wght@0,500;0,600;1,500&family=Montserrat:wght@400;500&display=swap">
<style>
  :root {
    --forest: #2f5e3a;
    --forest-deep: #24482c;
    --forest-light: #4b7d53;
    --gold: #e9dca2;
    --bronze: #b98e70;
    --paper: #f5f5f4;
    --slate: #4f5966;
    --stage: #d6d6d6;
    --ink: #1c2a1f;
  }
  * { margin: 0; padding: 0; box-sizing: border-box; }
  html, body { width: 1200px; height: 800px; overflow: hidden; }
  body {
    background: var(--stage);
    font-family: "Montserrat", sans-serif;
    position: relative;
  }
  .card {
    position: absolute;
    width: 540px;
    height: 308px;
    border-radius: 22px;
    overflow: hidden;
    background: var(--paper);
    top: 246px;
  }
  .card--contact { left: 40px; }
  .card--services { left: 620px; }

  .contact-bg { position: absolute; inset: 0; }

  .contact-details {
    position: absolute;
    left: 34px;
    top: 62px;
    color: #fff;
  }
  .contact-name {
    font-family: "Cormorant Garamond", serif;
    font-weight: 600;
    font-size: 25px;
    letter-spacing: 1.5px;
    font-variant: small-caps;
    line-height: 1;
  }
  .contact-role { font-size: 11px; margin: 4px 0 10px; opacity: .92; }
  .contact-address { font-size: 11px; line-height: 1.45; margin-bottom: 8px; }
  .contact-lines { list-style: none; font-size: 11px; line-height: 1.6; }
  .contact-lines li { display: flex; align-items: center; gap: 8px; }
  .contact-lines svg { width: 11px; height: 11px; flex: none; }
  .contact-licence { font-size: 11px; margin-top: 8px; }

  .brand-name {
    font-family: "Cormorant Garamond", serif;
    font-weight: 600;
    color: var(--forest);
    text-align: center;
    line-height: 1.05;
  }
  .card--contact .brand-name {
    position: absolute;
    left: 320px;
    top: 96px;
    width: 210px;
    font-size: 26px;
  }
  .card--contact .brand-name small { display: block; font-size: 14px; letter-spacing: 1px; margin-top: 4px; }

  .services-brand {
    position: absolute;
    left: 0; right: 0; top: 26px;
    text-align: center;
  }
  .card--services .brand-name { font-size: 32px; }
  .card--services .brand-name small { display: block; font-size: 18px; letter-spacing: 1.5px; margin-top: 2px; }
  .brand-tagline {
    font-family: "Cormorant Garamond", serif;
    font-style: italic;
    font-weight: 500;
    font-size: 15px;
    color: var(--ink);
    margin-top: 4px;
  }
  .services-band {
    position: absolute;
    left: 0; right: 0; top: 148px;
    height: 94px;
    background: var(--forest);
    color: #fff;
    font-size: 13.5px;
    line-height: 1.5;
    text-align: center;
    padding-top: 6px;
  }
  .partners {
    position: absolute;
    left: 0; right: 0; top: 256px;
    display: flex;
    justify-content: center;
    align-items: center;
    gap: 18px;
    color: var(--slate);
    font-size: 15px;
    font-weight: 500;
  }
  .partners .divider { width: 1px; height: 16px; background: var(--slate); opacity: .6; }
  .partner { display: flex; align-items: center; gap: 6px; }
  .partner-dot { width: 10px; height: 10px; border-radius: 50%; background: var(--slate); }
</style>
</head>
<body>

<section class="card card--contact">
  <svg class="contact-bg" viewBox="0 0 540 308" aria-hidden="true">
    <defs>
      <linearGradient id="forestFade" x1="0" y1="1" x2="1" y2="0">
        <stop offset="0" stop-color="#4b7d53"/>
        <stop offset="1" stop-color="#24482c"/>
      </linearGradient>
    </defs>
    <rect width="540" height="308" fill="url(#forestFade)"/>
    <circle cx="440" cy="90" r="206" fill="#b98e70"/>
    <circle cx="440" cy="90" r="198" fill="#e9dca2"/>
    <circle cx="440" cy="90" r="188" fill="#f5f5f4"/>
  </svg>

  <div class="brand-name">Kestrel Lane<small>Flooring &amp; Interiors</small></div>

  <div class="contact-details">
    <h1 class="contact-name">Owen Mercer</h1>
    <p class="contact-role">Salesperson</p>
    <p class="contact-address">27 Kestrel Lane<br>Harlow Cove CA 93011</p>
    <ul class="contact-lines">
      <li><svg viewBox="0 0 12 12"><path d="M2.5 1h2l1 3-1.5 1a6 6 0 0 0 3 3l1-1.5 3 1v2c0 .6-.5 1-1 1A10 10 0 0 1 1.5 2c0-.5.4-1 1-1z" fill="#fff"/></svg>555.204.7716</li>
      <li><svg viewBox="0 0 12 12"><rect x="3" y="0.5" width="6" height="11" rx="1" fill="none" stroke="#fff"/><circle cx="6" cy="9.5" r=".7" fill="#fff"/></svg>555-318-0492</li>
      <li><svg viewBox="0 0 12 12"><rect x="1" y="4" width="10" height="6" rx="1" fill="#fff"/><rect x="3" y="1" width="6" height="3" fill="none" stroke="#fff"/></svg>555.469.2083</li>
      <li><svg viewBox="0 0 12 12"><rect x="1" y="2.5" width="10" height="7" fill="none" stroke="#fff"/><path d="M1 2.5l5 4 5-4" fill="none" stroke="#fff"/></svg>owen@kestrellaneflooring.com</li>
      <li><svg viewBox="0 0 12 12"><circle cx="6" cy="6" r="5" fill="none" stroke="#fff"/><path d="M1 6h10M6 1c2 2.5 2 7.5 0 10M6 1c-2 2.5-2 7.5 0 10" fill="none" stroke="#fff" stroke-width=".8"/></svg>kestrellaneflooring.com</li>
    </ul>
    <p class="contact-licence">CA Lic: 481736</p>
  </div>
</section>

<section class="card card--services">
  <div class="services-brand">
    <div class="brand-name">Kestrel Lane<small>Flooring &amp; Interiors</small></div>
    <p class="brand-tagline">Home Town Service Since 1979</p>
  </div>

  <div class="services-band">
    <p>Area Rugs • Blinds • Carpet • Cork • Hardwood • Laminate</p>
    <p>Sheers • Valances • Vinyl • Bed Spreads • Draperies • LVP/SPC</p>
    <p>Fabric • Motorized Shades • Pillows • Shutters • Upholstery • Verticals</p>
  </div>

  <div class="partners">
    <span class="partner">Brightwell Shades</span>
    <span class="divider"></span>
    <span class="partner">quib<span class="partner-dot"></span></span>
  </div>
</section>

</body>
</html>
```